CEO of company needs clear business card that stands out from the rest

I need a clear business card (standard credit card size) for the CEO/Founder of our company...Brightfield Counseling. We would like to see designs that use our logo colors, which are khaki, chocolate brown, and gray. The card should be an edgy design, maybe where half the card is transparent with curves on the card, or a textured card where the logo is transparent, I don't care much for white cards. The final design should communicate a funky, edgy, and modern look, as well as stand out to have the "WOW" factor. The information we need on the card would be Name, Title, Toll free number, Phone Number, address, email address, and website.

*PLEASE SEND FRONT AND BACK OF CARDS

Card is two sided front and back please give us your front and back designs

The card should be an edgy design, maybe where half the card is transparent with curves on the card, or a textured card where the logo is transparent, I don't care much for white cards. The final design should communicate a funky, edgy, and modern look, as well as stand out to have the "WOW" factor.

Please follow these guidelines for the card

SPECS (card):

2.125 (h) x 3.375 (w) card size after cut

2.375 (h) x 3.625 (w) card with bleed

300 dpi

cmyk

1/8 bleed

allow 1/8 border for live area

I will also attached the pdf for the information listed above which includes a diagram of the card

 

All the cards need to have rounded edges

I just updated a card as an example of how you can use different fonts on a single business card, look how the name is written in script, so what I am saying is make this a card you will be proud to design and put it in your portfolio 

Reason: this race is really close and I am working with 2 designers to fine tune their designs and the weekend is slowing us down

• Our Logo
MUST HAVE PARTS OF CARD THAT ARE TRANSPARENT. See ideas that are attached.
Card is two sided front and back
• The final design should communicate a funky, edgy, and modern look, as well as stand out to have the "WOW" factor. The information we need on the card would be Name, Title, Toll free number, Phone Number, address, email address, and website.

```html
<!DOCTYPE html>
<html lang="en">
<head>
<meta charset="utf-8">
<title>Brightfield Counseling – Business Card</title>
<link rel="stylesheet" href="https://fonts.googleapis.com/css2?family=Tenor+Sans&family=Quicksand:wght@500&display=swap">
<style>
  :root {
    --backdrop: #e6e9ec;
    --card: #c4c4c4;
    --brown: #9a5329;
    --gray: #7f7f7f;
    --ink: #2e2e2e;
    --silver-light: #e4eaec;
    --silver: #a9b2b5;
    --khaki: #b9ab86;
  }
  * { margin: 0; padding: 0; box-sizing: border-box; }
  html, body {
    width: 1027px;
    height: 1200px;
    overflow: hidden;
    background: var(--backdrop);
  }
  .stage {
    position: relative;
    width: 1027px;
    height: 1200px;
  }
  .card {
    position: absolute;
    top: 272px;
    width: 330px;
    height: 655px;
    background: var(--card);
    border-radius: 10px;
    overflow: hidden;
    font-family: "Tenor Sans", sans-serif;
  }
  .card--front { left: 170px; }
  .card--back { left: 526px; }

  /* Symbol areas: plain circle with a soft gradient in the mark's tones */
  .mark-area {
    position: absolute;
    border-radius: 50%;
    background: radial-gradient(circle at 38% 35%, var(--silver-light) 0%, var(--silver) 45%, var(--khaki) 75%, var(--brown) 100%);
    opacity: 0.85;
  }
  .card--front .mark-area {
    left: 30px;
    top: 312px;
    width: 250px;
    height: 250px;
  }
  .card--back .mark-area {
    left: 78px;
    top: 310px;
    width: 250px;
    height: 250px;
  }

  /* Front */
  .brand {
    position: absolute;
    top: 86px;
    left: 0;
    width: 100%;
    text-align: center;
  }
  .brand__name {
    font-weight: 400;
    font-size: 40px;
    line-height: 1.08;
    color: var(--brown);
  }
  .brand__tagline {
    margin-top: 10px;
    font-family: "Quicksand", sans-serif;
    font-weight: 500;
    font-size: 14px;
    letter-spacing: 0.6px;
    color: var(--ink);
  }

  /* Back */
  .contact {
    position: absolute;
    top: 72px;
    left: 21px;
    right: 10px;
    white-space: nowrap;
  }
  .contact__name {
    font-weight: 400;
    font-size: 24px;
    color: var(--brown);
    line-height: 1.1;
  }
  .contact__title {
    font-size: 15px;
    color: var(--gray);
    line-height: 1.2;
  }
  .contact__lines {
    margin-top: 26px;
    font-size: 14px;
    letter-spacing: -0.3px;
    line-height: 1.25;
    color: var(--brown);
    list-style: none;
  }
  .contact__address {
    margin-top: 20px;
    font-style: normal;
    font-size: 14px;
    letter-spacing: -0.3px;
    line-height: 1.25;
    color: var(--brown);
  }
  .website {
    position: absolute;
    left: 21px;
    bottom: 22px;
    font-size: 15px;
    letter-spacing: -0.2px;
    color: var(--ink);
  }
</style>
</head>
<body>
  <main class="stage">
    <section class="card card--front" aria-label="Card front">
      <div class="brand">
        <p class="brand__name">Brightfield<br>Counseling</p>
        <p class="brand__tagline">a pro active addiction center</p>
      </div>
      <div class="mark-area" role="img" aria-label="Area for the company symbol in silver and brown"></div>
    </section>

    <section class="card card--back" aria-label="Card back">
      <div class="contact">
        <h1 class="contact__name">Helen Marsh</h1>
        <p class="contact__title">Certified Specialist</p>
        <ul class="contact__lines">
          <li>toll free: 555-014-2290 ext (120)</li>
          <li>phone: 555-014-2291</li>
          <li>email: helen@brightfieldcounseling.com</li>
        </ul>
        <address class="contact__address">
          48 Alder Row, Suite 12<br>
          Fairview CA 90411 Lakeside
        </address>
      </div>
      <div class="mark-area" role="img" aria-label="Area for the large company symbol in silver and brown"></div>
      <p class="website">www.brightfieldcounseling.com</p>
    </section>
  </main>
</body>
</html>
```